BRIGHTWAY FILING ADVISOR - PATENT PROCESS FLOW

I need a visual for a graphical process flow which explains the patent process to a user when they land on my web page. This graphical process flow will be presented on my first page. See the attached powerpoint where you can use the text and then create visuals in line with the visuals that I pulled from powerpoint. And lastly, I know it states on your webpage that for whatever work I purchase from you team, I will own the copyrights to it. I also need your team to send me an e-mail which states, to the best of your teams knowledge, that all creations are original and were not taken (copied) from other authors work.

Target Market(s)

entrepreneurs - start-up companies - garage inventors

Font styles to use
Sans Serif

Colors
33a6d7
4381bb
33b8a4
fbee3e
fbed22
eea4c8
3277b5
0355a3
9bcb3c

Requirements
Nice to have
• l like high-tech oriented things/visuals, so providing my process flow with a high-tech look and feel would be great. Also, not sure if it matters or if your team is aware, but i did order a logo created by your company as well. If you want to use the logo in the process flow, then that is fine too. No problem if we don't use it but just wanted your team to know if you think it would be complimentary if we used my logo in the process flow, similar to how i re-used my business-suit guy with lightbulb in my powerpoint.

```html
<!DOCTYPE html>
<html lang="en">
<head>
<meta charset="utf-8">
<title>Brightway Filing Advisor – Patent Process Flow</title>
<link href="https://fonts.googleapis.com/css2?family=Montserrat:wght@500;600;700&display=swap" rel="stylesheet">
<style>
  :root{
    --c-amber:#f5a524;
    --c-orange:#ee5b26;
    --c-purple:#6a3f9c;
    --c-navy:#1c5f86;
    --c-teal:#3196b4;
    --c-pink:#d24fa8;
    --c-ink:#262626;
    --c-frame:#d9d9d9;
  }
  *{margin:0;padding:0;box-sizing:border-box}
  html,body{width:1200px;height:2550px;overflow:hidden}
  body{position:relative;font-family:"Montserrat",Arial,sans-serif;color:var(--c-ink);background:#2f2f2f}
  .section{position:absolute;left:0;width:1200px}
  .section--one{top:0;height:850px;background:radial-gradient(ellipse at 50% 35%,#777 0%,#4a4a4a 75%,#3f3f3f 100%)}
  .section--two{top:850px;height:818px;background:radial-gradient(ellipse at 50% 40%,#474747 0%,#3a3a3a 100%)}
  .section--three{top:1668px;height:882px;background:radial-gradient(ellipse at 50% 40%,#363636 0%,#2b2b2b 100%)}
  .section-title{position:absolute;left:0;width:1200px;text-align:center;color:#fff;font-weight:600;font-size:22px;letter-spacing:.2px}
  .panel{position:absolute;left:120px;width:960px;height:640px;background:#fff;box-shadow:0 6px 18px rgba(0,0,0,.35)}
  .panel::before{content:"";position:absolute;inset:8px;border:1px solid var(--c-frame);
    background:linear-gradient(125deg,#f6f6f7 0%,#efeff0 45%,#f5f5f6 46%,#ececed 100%)}
  .flow{position:absolute;left:0;top:0;width:1200px;height:2550px}
  .icon{fill:none;stroke:currentColor;stroke-width:2.2;stroke-linecap:round;stroke-linejoin:round}
  .icon-mark{fill:currentColor;stroke:none;font-family:"Montserrat",Arial,sans-serif;font-weight:700}
  .step{position:absolute;width:160px;margin-left:-80px;text-align:center;font-weight:600;font-size:11.5px;line-height:14.5px;text-transform:uppercase}
  .step--loose{line-height:16px}
  .step::after{content:"";display:block;width:20px;height:1.5px;background:var(--c-ink);margin:4px auto 0}
  .step-num{position:absolute;width:60px;margin-left:-30px;text-align:center;font-weight:600;font-size:15px}
  .patent-label{position:absolute;width:120px;margin-left:-60px;text-align:center;font-weight:600;font-size:15px}
  .amber{color:var(--c-amber)} .orange{color:var(--c-orange)} .purple{color:var(--c-purple)}
  .navy{color:var(--c-navy)} .teal{color:var(--c-teal)} .pink{color:var(--c-pink)}
</style>
</head>
<body>

<section class="section section--one"><h2 class="section-title" style="top:64px">Graphic-1</h2></section>
<section class="section section--two"><h2 class="section-title" style="top:40px">Graphic-2</h2></section>
<section class="section section--three"><h2 class="section-title" style="top:60px">Graphic-3</h2></section>

<div class="panel" style="top:125px"></div>
<div class="panel" style="top:943px"></div>
<div class="panel" style="top:1792px"></div>

<svg class="flow" viewBox="0 0 1200 2550" xmlns="http://www.w3.org/2000/svg">
  <defs>
    <filter id="soft-shadow" x="-30%" y="-30%" width="160%" height="160%">
      <feDropShadow dx="0" dy="3" stdDeviation="3" flood-color="#000" flood-opacity=".18"/>
    </filter>
    <g id="node-base"><circle r="57" fill="#fff" filter="url(#soft-shadow)"/></g>

    <symbol id="ic-bulb" viewBox="0 0 64 64" class="icon">
      <path d="M32 12a13 13 0 0 0-8 23.3c1.6 1.3 2.5 3 2.5 5V43h11v-2.7c0-2 .9-3.7 2.5-5A13 13 0 0 0 32 12z"/>
      <path d="M26 47h12M27 51h10M29 55h6M32 3v4M14 14l3 3M50 14l-3 3M8 28h4M52 28h4"/>
      <path d="M28 31l4-4 4 4M32 27v16"/>
    </symbol>
    <symbol id="ic-headset" viewBox="0 0 64 64" class="icon">
      <path d="M16 36v-6a16 16 0 0 1 32 0v6"/>
      <rect x="11" y="34" width="9" height="13" rx="3"/><rect x="44" y="34" width="9" height="13" rx="3"/>
      <path d="M48 47c0 6-6 9-12 9"/><rect x="29" y="53" width="7" height="6" rx="2"/>
      <path d="M32 6v3M24 8l1.5 2.5M40 8l-1.5 2.5"/>
    </symbol>
    <symbol id="ic-exchange" viewBox="0 0 64 64" class="icon">
      <circle cx="22" cy="23" r="11"/><text x="22" y="28" font-size="14" text-anchor="middle" class="icon-mark">$</text>
      <circle cx="42" cy="41" r="11"/><text x="42" y="46" font-size="14" text-anchor="middle" class="icon-mark">$</text>
      <path d="M38 12h12v10M46 18l4 4 4-4"/><path d="M26 52H14V42M10 46l4-4 4 4"/>
    </symbol>
    <symbol id="ic-chat" viewBox="0 0 64 64" class="icon">
      <path d="M8 10h30v20H22l-7 6v-6H8z"/><path d="M15 17h16M15 23h10"/>
      <path d="M42 22h14v20h-7v6l-7-6H28v-8"/><path d="M34 48h-26M8 48v8M50 48v8"/>
    </symbol>
    <symbol id="ic-network" viewBox="0 0 64 64" class="icon">
      <circle cx="32" cy="29" r="9"/><path d="M28 38h8v6h-8zM30 48h4"/>
      <circle cx="11" cy="12" r="4.5"/><circle cx="53" cy="12" r="4.5"/><circle cx="11" cy="50" r="4.5"/><circle cx="53" cy="50" r="4.5"/>
      <path d="M15 15l10 8M49 15l-10 8M15 47l10-7M49 47l-10-7"/>
    </symbol>
    <symbol id="ic-beacon" viewBox="0 0 64 64" class="icon">
      <path d="M20 46V31a12 12 0 0 1 24 0v15"/><path d="M26 31a6 6 0 0 1 6-6"/>
      <rect x="14" y="46" width="36" height="7" rx="1"/><path d="M10 58h44M32 5v7M14 13l4 4M50 13l-4 4M5 30h7M52 30h7"/>
    </symbol>
    <symbol id="ic-circuit-bulb" viewBox="0 0 64 64" class="icon">
      <path d="M32 8a15 15 0 0 0-9 27c1.7 1.4 2.6 3.2 2.6 5.3V43h12.8v-2.7c0-2.1.9-3.9 2.6-5.3A15 15 0 0 0 32 8z"/>
      <path d="M26 47h12M27 51h10M29 55h6"/>
      <path d="M32 16v22M32 24l-6-4M32 30l6-4M32 34l-5 2"/>
      <circle cx="25" cy="19" r="1.8"/><circle cx="39" cy="25" r="1.8"/><circle cx="26" cy="37" r="1.8"/>
      <path d="M8 12l2 2M54 12l-2 2M6 26h3M55 26h3"/>
    </symbol>
    <symbol id="ic-monitor" viewBox="0 0 64 64" class="icon">
      <rect x="8" y="12" width="48" height="32" rx="2"/><path d="M8 38h48M27 44l-2 8h14l-2-8M20 52h24"/>
      <rect x="14" y="17" width="24" height="16" rx="1"/><path d="M34 24l9 8-4 1 2.5 4-2.2 1.2-2.4-4-3 3z"/>
    </symbol>
    <symbol id="ic-doc-gear" viewBox="0 0 64 64" class="icon">
      <path d="M14 6h26l10 10v42H14z"/><path d="M40 6v10h10"/>
      <circle cx="32" cy="25" r="5"/><path d="M32 16v3M32 31v3M23 25h3M38 25h3M26 19l2 2M36 29l2 2M38 19l-2 2M28 29l-2 2"/>
      <path d="M20 40h24M20 46h18M20 52h10"/>
    </symbol>
    <symbol id="ic-building" viewBox="0 0 64 64" class="icon">
      <rect x="20" y="8" width="22" height="48"/><rect x="42" y="22" width="12" height="34"/><rect x="10" y="30" width="10" height="26"/>
      <path d="M25 15v4M31 15v4M37 15v4M25 25v4M31 25v4M37 25v4M25 35v4M31 35v4M37 35v4M48 28v4M48 38v4M15 36v4M15 46v4M4 56h56"/>
      <path d="M27 56v-9h8v9"/>
    </symbol>
    <symbol id="ic-doc-check" viewBox="0 0 64 64" class="icon">
      <path d="M12 6h28v46H12z"/><path d="M18 14h16M18 20h16M18 26h12M18 32h8M18 38h6"/>
      <circle cx="44" cy="44" r="11"/><path d="M38.5 44l4 4 6.5-7.5"/>
    </symbol>
    <symbol id="ic-money-chart" viewBox="0 0 64 64" class="icon">
      <rect x="6" y="34" width="52" height="22" rx="2"/><circle cx="32" cy="45" r="7"/>
      <text x="32" y="49.5" font-size="12" text-anchor="middle" class="icon-mark">$</text>
      <path d="M12 40v10M52 40v10"/>
      <path d="M12 34v-6h8v6M26 34V22h8v12M40 34V16h8v18"/><path d="M40 10l4-5 4 5M44 5v9"/>
    </symbol>
    <symbol id="ic-form-pen" viewBox="0 0 64 64" class="icon">
      <rect x="10" y="8" width="32" height="48" rx="2"/><path d="M17 18h18M17 26h18M17 34h18M17 42h10"/>
      <path d="M50 16l6 6-18 18-8 2 2-8z"/><path d="M46 20l6 6"/>
    </symbol>
    <symbol id="ic-briefcase" viewBox="0 0 64 64" class="icon">
      <rect x="8" y="20" width="48" height="32" rx="3"/><path d="M24 20v-6h16v6M8 33h48M28 33v5h8v-5"/>
      <path d="M12 8l3 3M52 8l-3 3M32 4v4"/>
    </symbol>
    <symbol id="ic-money-stack" viewBox="0 0 64 64" class="icon">
      <rect x="6" y="12" width="52" height="26" rx="3"/><circle cx="32" cy="25" r="8"/>
      <text x="32" y="30" font-size="13" text-anchor="middle" class="icon-mark">$</text>
      <path d="M13 19v12M51 19v12M6 44h52M6 50h52M6 56h52"/>
    </symbol>
  </defs>

  <!-- Graphic 1 connectors -->
  <g fill="none" stroke="var(--c-teal)" stroke-width="1.6">
    <polyline points="968,308 1044,308 1044,591 956,591"/>
    <polyline points="1036,440 1044,448 1052,440"/><polyline points="1036,446 1044,454 1052,446"/>
    <polyline points="943,584 935,591 943,598"/><polyline points="949,584 941,591 949,598"/>
    <line x1="159" y1="599" x2="356" y2="599"/>
    <line x1="488" y1="599" x2="528" y2="599"/>
    <line x1="662" y1="599" x2="704" y2="599"/>
    <line x1="838" y1="599" x2="922" y2="599"/>
  </g>
  <circle cx="159" cy="599" r="4" fill="var(--c-teal)"/>

  <!-- Graphic 3 link lines -->
  <g stroke="var(--c-navy)" stroke-width="1.6">
    <line x1="732" y1="2010" x2="772" y2="2024"/>
    <line x1="722" y1="2042" x2="762" y2="2058"/>
  </g>

  <!-- Graphic 1 nodes -->
  <g transform="translate(290,308)" stroke="var(--c-amber)" fill="none" stroke-width="1.8">
    <path d="M-30,58 A65,65 0 1 1 50,-42"/><polyline points="36,-66 44,-72 78,-72 78,-16"/><polyline points="30,-72 38,-72 34,-78"/>
    <use href="#node-base" stroke="none"/>
    <use href="#ic-bulb" x="-30" y="-30" width="60" height="60" style="color:var(--c-amber)" role="img" aria-label="Idea icon"/>
  </g>
  <g transform="translate(441,253)" stroke="var(--c-orange)" fill="none" stroke-width="1.8">
    <path d="M-58,30 A65,65 0 1 1 60,24"/><polyline points="62,26 72,32 72,78 34,78"/><polyline points="40,72 32,78 40,84"/>
    <use href="#node-base" stroke="none"/>
    <use href="#ic-headset" x="-30" y="-30" width="60" height="60" style="color:var(--c-orange)" role="img" aria-label="Call icon"/>
  </g>
  <g transform="translate(589,308)" stroke="var(--c-purple)" fill="none" stroke-width="1.8">
    <path d="M-30,58 A65,65 0 1 1 50,-42"/><polyline points="36,-66 44,-72 78,-72 78,-16"/><polyline points="30,-72 38,-72 34,-78"/>
    <use href="#node-base" stroke="none"/>
    <use href="#ic-exchange" x="-30" y="-30" width="60" height="60" style="color:var(--c-purple)" role="img" aria-label="Payment icon"/>
  </g>
  <g transform="translate(738,253)" stroke="var(--c-navy)" fill="none" stroke-width="1.8">
    <path d="M-58,30 A65,65 0 1 1 60,24"/><polyline points="62,26 72,32 72,78 34,78"/><polyline points="40,72 32,78 40,84"/>
    <use href="#node-base" stroke="none"/>
    <use href="#ic-chat" x="-30" y="-30" width="60" height="60" style="color:var(--c-navy)" role="img" aria-label="Discussion icon"/>
  </g>
  <g transform="translate(894,308)" stroke="var(--c-teal)" fill="none" stroke-width="1.8">
    <circle r="65"/><use href="#node-base" stroke="none"/>
    <use href="#ic-network" x="-30" y="-30" width="60" height="60" style="color:var(--c-teal)" role="img" aria-label="Search network icon"/>
  </g>
  <g transform="translate(421,596)" stroke="var(--c-teal)" fill="none" stroke-width="1.8">
    <circle r="65"/><use href="#node-base" stroke="none"/>
    <use href="#ic-beacon" x="-30" y="-30" width="60" height="60" style="color:var(--c-teal)" role="img" aria-label="Alert beacon icon"/>
  </g>
  <g transform="translate(595,596)" stroke="var(--c-teal)" fill="none" stroke-width="1.8">
    <circle r="65"/><use href="#node-base" stroke="none"/>
    <use href="#ic-circuit-bulb" x="-30" y="-30" width="60" height="60" style="color:var(--c-teal)" role="img" aria-label="Circuit bulb icon"/>
  </g>
  <g transform="translate(771,596)" stroke="var(--c-teal)" fill="none" stroke-width="1.8">
    <circle r="65"/><use href="#node-base" stroke="none"/>
    <use href="#ic-bulb" x="-30" y="-30" width="60" height="60" style="color:var(--c-teal)" role="img" aria-label="Light bulb icon"/>
  </g>

  <!-- Graphic 2 nodes -->
  <g transform="translate(219,1205)" stroke="var(--c-amber)" fill="none" stroke-width="1.8">
    <path d="M-30,58 A65,65 0 1 1 50,-42"/><polyline points="36,-66 44,-72 78,-72 78,-16"/><polyline points="30,-72 38,-72 34,-78"/>
    <use href="#node-base" stroke="none"/>
    <use href="#ic-network" x="-30" y="-30" width="60" height="60" style="color:var(--c-amber)" role="img" aria-label="Idea review icon"/>
  </g>
  <g transform="translate(371,1150)" stroke="var(--c-orange)" fill="none" stroke-width="1.8">
    <path d="M-58,30 A65,65 0 1 1 60,24"/><polyline points="62,26 72,32 72,78 34,78"/><polyline points="40,72 32,78 40,84"/>
    <use href="#node-base" stroke="none"/>
    <use href="#ic-monitor" x="-30" y="-30" width="60" height="60" style="color:var(--c-orange)" role="img" aria-label="Computer icon"/>
  </g>
  <g transform="translate(521,1205)" stroke="var(--c-purple)" fill="none" stroke-width="1.8">
    <path d="M-30,58 A65,65 0 1 1 50,-42"/><polyline points="36,-66 44,-72 78,-72 78,-16"/><polyline points="30,-72 38,-72 34,-78"/>
    <use href="#node-base" stroke="none"/>
    <use href="#ic-doc-gear" x="-30" y="-30" width="60" height="60" style="color:var(--c-purple)" role="img" aria-label="Manual icon"/>
  </g>
  <g transform="translate(668,1150)" stroke="var(--c-navy)" fill="none" stroke-width="1.8">
    <path d="M-58,30 A65,65 0 1 1 60,24"/><polyline points="62,26 72,32 72,78 34,78"/><polyline points="40,72 32,78 40,84"/>
    <use href="#node-base" stroke="none"/>
    <use href="#ic-building" x="-30" y="-30" width="60" height="60" style="color:var(--c-navy)" role="img" aria-label="Office icon"/>
  </g>
  <g transform="translate(818,1205)" stroke="var(--c-teal)" fill="none" stroke-width="1.8">
    <path d="M-30,58 A65,65 0 1 1 50,-42"/><polyline points="36,-66 44,-72 78,-72 78,-16"/><polyline points="30,-72 38,-72 34,-78"/>
    <use href="#node-base" stroke="none"/>
    <use href="#ic-doc-check" x="-30" y="-30" width="60" height="60" style="color:var(--c-teal)" role="img" aria-label="Approved document icon"/>
  </g>
  <g transform="translate(965,1205)" stroke="var(--c-pink)" fill="none" stroke-width="1.8">
    <circle r="65"/><use href="#node-base" stroke="none"/>
    <use href="#ic-money-chart" x="-30" y="-30" width="60" height="60" style="color:var(--c-pink)" role="img" aria-label="Funding growth icon"/>
  </g>

  <!-- Graphic 3 nodes -->
  <g transform="translate(219,2055)" stroke="var(--c-amber)" fill="none" stroke-width="1.8">
    <path d="M-30,58 A65,65 0 1 1 50,-42"/><polyline points="36,-66 44,-72 78,-72 78,-16"/><polyline points="30,-72 38,-72 34,-78"/>
    <use href="#node-base" stroke="none"/>
    <use href="#ic-exchange" x="-30" y="-30" width="60" height="60" style="color:var(--c-amber)" role="img" aria-label="Payment icon"/>
  </g>
  <g transform="translate(368,2000)" stroke="var(--c-orange)" fill="none" stroke-width="1.8">
    <path d="M-58,30 A65,65 0 1 1 60,24"/><polyline points="62,26 72,32 72,78 34,78"/><polyline points="40,72 32,78 40,84"/>
    <use href="#node-base" stroke="none"/>
    <use href="#ic-form-pen" x="-30" y="-30" width="60" height="60" style="color:var(--c-orange)" role="img" aria-label="Application form icon"/>
  </g>
  <g transform="translate(520,2055)" stroke="var(--c-purple)" fill="none" stroke-width="1.8">
    <path d="M-30,58 A65,65 0 1 1 50,-42"/><polyline points="36,-66 44,-72 78,-72 78,-16"/><polyline points="30,-72 38,-72 34,-78"/>
    <use href="#node-base" stroke="none"/>
    <use href="#ic-building" x="-30" y="-30" width="60" height="60" style="color:var(--c-purple)" role="img" aria-label="Office icon"/>
  </g>
  <g transform="translate(670,1998)" stroke="var(--c-navy)" fill="none" stroke-width="1.8">
    <circle r="65"/><use href="#node-base" stroke="none"/>
    <use href="#ic-briefcase" x="-30" y="-30" width="60" height="60" style="color:var(--c-navy)" role="img" aria-label="Advisor icon"/>
  </g>
  <g transform="translate(818,2055)" stroke="var(--c-teal)" fill="none" stroke-width="1.8">
    <path d="M-30,58 A65,65 0 1 1 50,-42"/><polyline points="36,-66 44,-72 78,-72 78,-16"/><polyline points="30,-72 38,-72 34,-78"/>
    <use href="#node-base" stroke="none"/>
    <use href="#ic-building" x="-30" y="-30" width="60" height="60" style="color:var(--c-teal)" role="img" aria-label="Office icon"/>
  </g>
  <g transform="translate(965,2055)" stroke="var(--c-pink)" fill="none" stroke-width="1.8">
    <circle r="65"/><use href="#node-base" stroke="none"/>
    <use href="#ic-money-stack" x="-30" y="-30" width="60" height="60" style="color:var(--c-pink)" role="img" aria-label="Money icon"/>
  </g>
</svg>

<!-- Graphic 1 labels -->
<div class="step-num amber" style="left:291px;top:384px">01</div>
<div class="step step--loose" style="left:293px;top:408px">Idea stage</div>
<div class="step-num orange" style="left:428px;top:384px">02</div>
<div class="step step--loose" style="left:428px;top:408px">Call Brightway Filing<br>Advisor &amp; discuss<br>your idea.</div>
<div class="step-num purple" style="left:587px;top:383px">03</div>
<div class="step step--loose" style="left:587px;top:405px;width:150px;margin-left:-75px">Discuss how you make money with a patent. Ready to pay for patent search on idea?</div>
<div class="step-num navy" style="left:745px;top:383px">04</div>
<div class="step step--loose" style="left:748px;top:405px;width:160px">Describe your idea in detail with writing and pay for patent search.</div>
<div class="step-num teal" style="left:900px;top:383px">05</div>
<div class="step step--loose" style="left:905px;top:405px;width:150px;margin-left:-75px">Brightway Filing Advisor orders patent search to find other patents close to your idea.</div>
<div class="patent-label" style="left:419px;top:671px">PAT. NO. 3</div>
<div class="patent-label" style="left:592px;top:671px">PAT. NO. 2</div>
<div class="patent-label" style="left:774px;top:671px">PAT. NO. 1</div>

<!-- Graphic 2 labels -->
<div class="step-num amber" style="left:219px;top:1281px">01</div>
<div class="step" style="left:221px;top:1305px;width:155px;margin-left:-77px">You and Brightway Filing Advisor determine if idea is different enough (patentable) compared to other patents.</div>
<div class="step-num orange" style="left:375px;top:1281px">02</div>
<div class="step" style="left:380px;top:1305px;width:145px;margin-left:-72px">If idea is different enough (patentable), then you pay Brightway Filing Advisor to help you with writing provisional patent application.</div>
<div class="step-num purple" style="left:527px;top:1281px">03</div>
<div class="step" style="left:533px;top:1305px;width:140px;margin-left:-70px">Every patent application is a user manual for your idea: how do you make the idea and use the idea – 10 pages minimum.</div>
<div class="step-num navy" style="left:674px;top:1280px">04</div>
<div class="step" style="left:677px;top:1305px;width:130px;margin-left:-65px">File your provisional patent application in patent office.</div>
<div class="step-num teal" style="left:817px;top:1281px">05</div>
<div class="step" style="left:820px;top:1305px;width:135px;margin-left:-67px">Patent office receives your provisional patent application and keeps application for 1 year.</div>
<div class="step-num pink" style="left:972px;top:1280px">06</div>
<div class="step" style="left:965px;top:1305px;width:140px;margin-left:-70px">During next 6 months, raise money for business behind idea and to create budget for full patent application.</div>

<!-- Graphic 3 labels -->
<div class="step-num amber" style="left:219px;top:2130px">01</div>
<div class="step" style="left:221px;top:2154px;width:140px;margin-left:-70px;line-height:16px">Pay Brightway Filing Advisor at 6months post provisional to prepare full patent application.</div>
<div class="step-num orange" style="left:375px;top:2130px">02</div>
<div class="step" style="left:380px;top:2154px;width:140px;margin-left:-70px;line-height:16px">Full patent application prepared by Brightway Filing Advisor follows patent rules and procedures and has claims. 20 pages.</div>
<div class="step-num purple" style="left:527px;top:2130px">03</div>
<div class="step" style="left:533px;top:2154px;width:130px;margin-left:-65px">File full patent application in patent office before 1year mark relative to provisional application.</div>
<div class="step-num navy" style="left:730px;top:2130px">04</div>
<div class="step" style="left:732px;top:2156px;width:130px;margin-left:-65px">Brightway Filing Advisor negotiates over 2-3 years with patent office to get your patent.</div>
<div class="step-num pink" style="left:965px;top:2130px">05</div>
<div class="step" style="left:965px;top:2154px;width:145px;margin-left:-72px">Once you have your patent 3years later, with help of Brightway Filing Advisor, you can sell patent or license patent to others for money.</div>

</body>
</html>
```